Packaging design for a low carb bar

I am producing a low carb / high fat bar, therefore I would like to have a light weighted modern design. The background color pastel light or something like that. The package should be focused on fitness-active individuals who are looking for healthy low carb snacks. Preliminary packaging size, logo, and more details on what should be attached to the packaging are attached. Thank you!

```html
<!DOCTYPE html>
<html lang="en">
<head>
<meta charset="utf-8">
<title>Verdane Fuel Almond Keto Bar Wrapper</title>
<link href="https://fonts.googleapis.com/css2?family=Rajdhani:wght@400;500;600&display=swap" rel="stylesheet">
<style>
  :root {
    --backdrop: #208a9a;
    --teal: #1f8796;
    --teal-deep: #176f7c;
    --teal-crimp: #2a8e9c;
    --panel: #eeeeed;
    --panel-edge: #e4e2df;
    --crimp-light: #dcd6cf;
    --ink: #2b2b2b;
    --ink-soft: #4a4a4a;
  }
  * { margin: 0; padding: 0; box-sizing: border-box; }
  html, body { width: 1200px; height: 849px; overflow: hidden; }
  body {
    background: var(--backdrop);
    font-family: "Rajdhani", sans-serif;
    position: relative;
  }
  .wrapper {
    position: absolute;
    left: 187px; top: 328px;
    width: 829px; height: 196px;
    background: var(--panel);
    overflow: hidden;
  }
  .crimp-left {
    position: absolute; left: 0; top: 0; width: 83px; height: 100%;
    background: repeating-linear-gradient(90deg, var(--teal-crimp) 0 6px, var(--teal-deep) 6px 8px);
  }
  .product-photo {
    position: absolute; left: 83px; top: 0; width: 250px; height: 100%;
    background: linear-gradient(120deg, #3b3029 0%, #6b5a4b 35%, #4f7479 65%, #2f5a60 100%);
  }
  .photo-fade {
    position: absolute; left: 333px; top: 0; width: 26px; height: 100%;
    background: linear-gradient(90deg, #1d3d42 0%, #8fa7aa 55%, var(--panel) 100%);
  }
  .flavour {
    position: absolute; left: 372px; top: 98px;
    transform: translate(-50%, -50%) rotate(-90deg);
    font-size: 40px; font-weight: 600; letter-spacing: 3px;
    color: var(--teal); white-space: nowrap;
  }
  .brand {
    position: absolute; left: 576px; top: 44px; width: 0;
    display: flex; align-items: center; justify-content: center; gap: 8px;
    white-space: nowrap;
  }
  .brand-dot { width: 14px; height: 14px; border-radius: 50%; background: var(--teal); flex: none; }
  .brand-name { font-size: 26px; font-weight: 500; letter-spacing: 2px; color: var(--teal); }
  .product-name {
    position: absolute; left: 0; width: 1152px; top: 124px; text-align: center;
    font-size: 31px; font-weight: 500; color: var(--ink); white-space: nowrap;
  }
  .product-name .accent { color: var(--teal); }
  .info-row {
    position: absolute; left: 395px; top: 166px;
    display: flex; align-items: flex-start;
    font-size: 13px; color: var(--ink-soft); line-height: 1.15;
  }
  .info-row .cell { padding: 0 12px; }
  .info-row .cell + .cell { border-left: 1.5px solid var(--teal); }
  .crimp-right {
    position: absolute; right: 0; top: 0; width: 78px; height: 100%;
    background: repeating-linear-gradient(180deg, var(--crimp-light) 0 5px, #cbc4bb 5px 7px);
  }
  .ingredients {
    position: absolute; left: 38px; top: 98px;
    transform: translate(-50%, -50%) rotate(-90deg);
    white-space: nowrap; text-align: left;
  }
  .ingredients-title { font-size: 20px; font-weight: 600; letter-spacing: 1px; color: var(--teal); line-height: 1; }
  .ingredients-list { font-size: 11px; color: var(--ink-soft); line-height: 1.2; margin-top: 2px; }
</style>
</head>
<body>
  <div class="wrapper">
    <div class="crimp-left"></div>
    <div class="product-photo" role="img" aria-label="Photo of almonds scattered on a rustic wooden table"></div>
    <div class="photo-fade"></div>
    <div class="flavour">ALMOND</div>

    <div class="brand">
      <span class="brand-dot"></span>
      <span class="brand-name">VERDANE FUEL</span>
    </div>

    <div class="product-name"><span class="accent">KETO</span> BAR</div>

    <div class="info-row">
      <div class="cell">Suitable for a<br>low carb diet</div>
      <div class="cell">3.5g Net</div>
      <div class="cell">Vegan</div>
    </div>

    <div class="crimp-right">
      <div class="ingredients">
        <div class="ingredients-title">INGREDIENTS</div>
        <div class="ingredients-list">Peanuts, Almonds, Chia,<br>Coconut Sunflower &amp;<br>Pumpkin Seeds.</div>
      </div>
    </div>
  </div>
</body>
</html>
```